oloperra Web Design Project

It is a virtual assistance/concierge company that helps the busy professional by remotely providing administrative, technical and/or creative business support services, specializing in the medical device industry. Company name is oloperra.
(website will be oloperra.example)

Allowing things to be done without taking time away from more urgent issues or family/personal time. Partnering with a VA reduces stress, protects cash flow, eliminates administrative hassles, and enables business people to find the success they originally set out to achieve. Saves small businesses and/or individuals on overhead, salary, et. Work is done remotely to offer administrative, clerical, typing and specialist service assistance on a regular, ad-hoc or emergency cover basis.

Though we are capable of addressing the needs of medical professionals and industry representatives due to our experience and knowledge (sales, HCC guidelines, etc.) we do not want to be limited to that market only.

Target Market(s)

Target market would be M/F, 30-50, National, busy, Alpha, entrepreneurs and industry professionals who want/need to do more without sacrifice of life

Industry/Entity Type

Industry

Requirements
Nice to have
• We do have a logo designed via the MakerFolk website that can/should be included. Logo is uploaded.

```html
<!DOCTYPE html>
<html lang="en">
<head>
<meta charset="utf-8">
<title>oloperra</title>
<link rel="stylesheet" href="https://fonts.googleapis.com/css2?family=Arimo:wght@400;700&display=swap">
<style>
:root{
  --page-grey:#f6f6f6;
  --white:#ffffff;
  --brand-red:#e2000f;
  --deep-red:#c20008;
  --brand-navy:#00224a;
  --deep-navy:#000d28;
  --nav-grey:#b7c1cd;
  --text:#3a3a3a;
  --muted:#7a8794;
  --rule:#cfcfcf;
}
*{box-sizing:border-box;margin:0;padding:0}
html,body{width:1200px;height:1185px;overflow:hidden}
body{position:relative;background:var(--white);font-family:"Arimo",Arial,sans-serif;color:var(--text)}
.header-band{position:absolute;left:0;top:0;width:1200px;height:584px;background:var(--page-grey)}
.brand{position:absolute;left:20px;top:40px;display:flex;align-items:center;gap:12px}
.brand-dot{width:34px;height:34px;border-radius:50%;background:var(--brand-red)}
.brand-name{font-size:58px;font-weight:700;color:var(--brand-navy);letter-spacing:-1px;line-height:1}
.main-nav{position:absolute;left:552px;top:58px;width:629px;height:38px;display:flex;background:var(--nav-grey)}
.main-nav a{display:flex;align-items:center;justify-content:center;height:100%;font-size:18px;color:var(--brand-navy);text-decoration:none}
.main-nav a.active{background:var(--brand-red);color:var(--white);width:100px}
.main-nav .n-about{width:118px}.main-nav .n-services{width:124px}.main-nav .n-testi{width:150px}.main-nav .n-contact{width:137px}
.hero{position:absolute;left:20px;top:142px;width:1161px;height:415px;border:1px solid #a9a9a9;
  background:linear-gradient(100deg,#e9ecef 0%,#f7f7f7 30%,#ffffff 55%,#eef6f0 80%,#e3efe6 100%)}
.service-card{position:absolute;top:610px;width:560px;height:205px;color:var(--white)}
.service-card.admin{left:20px;background:var(--brand-red)}
.service-card.tech{left:621px;background:var(--brand-navy)}
.service-card h2{position:absolute;left:12px;top:12px;right:0;height:47px;padding-left:9px;font-weight:400;font-size:29px;line-height:47px}
.admin h2{background:var(--deep-red)}
.tech h2{background:var(--deep-navy)}
.service-photo{position:absolute;left:20px;top:66px;width:212px;height:118px}
.admin .service-photo{background:linear-gradient(90deg,#c9ccd2,#f2f2f2 50%,#a9adb4)}
.tech .service-photo{background:linear-gradient(90deg,#d8dade,#f4f4f4 50%,#cfd2d6)}
.service-card p{position:absolute;left:244px;top:70px;width:300px;font-size:15.4px;line-height:21.3px;letter-spacing:.2px}
.section-title{font-size:29px;font-weight:400;color:var(--brand-navy);line-height:1}
.about{position:absolute;left:20px;top:843px;width:676px}
.about p{margin-top:8px;font-size:15.4px;line-height:21.3px;letter-spacing:.35px}
.read-more{position:absolute;top:1074px;font-size:13px;line-height:16px;color:var(--muted);text-decoration:none;letter-spacing:.3px}
.read-more.about-more{left:636px}
.read-more.news-more{left:1112px}
.divider{position:absolute;left:719px;top:843px;width:1px;height:247px;background:var(--rule)}
.news{position:absolute;left:740px;top:843px;width:436px}
.news-list{list-style:none;margin-top:8px;border-top:1px solid var(--rule)}
.news-list li{border-bottom:1px solid var(--rule);padding:6px 0 10px}
.news-date{display:block;font-weight:700;font-size:15.4px;color:var(--brand-navy);line-height:22px;letter-spacing:.3px}
.news-list p{width:425px;font-size:15.4px;line-height:19px;letter-spacing:.3px}
.site-footer{position:absolute;left:0;top:1105px;width:1200px;height:80px;background:var(--page-grey);text-align:center;font-size:13px;color:#777;padding-top:35px}
</style>
</head>
<body>
<div class="header-band"></div>
<div class="brand"><span class="brand-dot"></span><span class="brand-name">oloperra</span></div>
<nav class="main-nav">
  <a class="active" href="#">Home</a>
  <a class="n-about" href="#">About us</a>
  <a class="n-services" href="#">Services</a>
  <a class="n-testi" href="#">Teatimonials</a>
  <a class="n-contact" href="#">Contact us</a>
</nav>
<div class="hero" role="img" aria-label="Photo of an assistant at a desk on the phone beside a laptop, with a calendar and pencil"></div>

<section class="service-card admin">
  <h2>Administrative</h2>
  <div class="service-photo" role="img" aria-label="Photo of a smiling business team in an office"></div>
  <p>Lorem Ipsum is simply dummy text of the printing and typesetting industry. Lorem Ipsum has been the industry's standard dummy text and scrambled it to make a type specimen book.....</p>
</section>
<section class="service-card tech">
  <h2>Technical support</h2>
  <div class="service-photo" role="img" aria-label="Photo of three support team members"></div>
  <p>Lorem Ipsum is simply dummy text of the printing and typesetting industry. Lorem Ipsum has been the industry's standard dummy text and scrambled it to make a type specimen book......</p>
</section>

<section class="about">
  <h2 class="section-title">About us</h2>
  <p>Lorem Ipsum is simply dummy text of the printing and typesetting industry. Lorem Ipsum has been the industry's standard dummy text ever since the 1500s, when an unknown printer took a galley of type and scrambled it to make a type specimen book. Lorem Ipsum is simply dummy text of the printing and typesetting industry. Lorem Ipsum has been the industry's standard dummy text ever since the 1500s, when an unknown printer took a galley of type and scrambled it to make a type specimen book. Lorem Ipsum is simply dummy text of the printing and typesetting industry. Lorem Ipsum has been the industry's standard dummy text ever since the 1500s, when an unknown printer took a galley of type and scrambled it to make a type specimen book.</p>
</section>
<a class="read-more about-more" href="#">read more</a>
<div class="divider"></div>

<section class="news">
  <h2 class="section-title">Latest News</h2>
  <ul class="news-list">
    <li><span class="news-date">10-12-12 :</span><p>Lorem Ipsum is simply dummy text of the printing and type-setting industry. Lorem Ipsum has been the industry's standard dummy text</p></li>
    <li><span class="news-date">10-12-12 :</span><p>Lorem Ipsum is simply dummy text of the printing and type-setting industry. Lorem Ipsum has been the industry's standard dummy text</p></li>
  </ul>
</section>
<a class="read-more news-more" href="#">read more</a>

<footer class="site-footer">© 2012 - Terms of Service - Privacy Policy - Program Policies</footer>
</body>
</html>
```